KTR Associates Business Card

I would like to have a business card designed that uses my current logo and colors. I am not looking for anything to "out there" but can have a little fun so that it stands out.

I have a boutique consulting firm that specializes in strategic planning, change management, leadership development and innovation.

Industry/Entity Type

Leadership

Contact Information for Business Card

Marta Holbeck
President
marta@ktr-associates.example
555-014-2286

```html
<!DOCTYPE html>
<html lang="en">
<head>
<meta charset="utf-8">
<title>KTR Associates Business Card</title>
<link href="https://fonts.googleapis.com/css2?family=Jost:wght@300;400;700&display=swap" rel="stylesheet">
<style>
  :root {
    --page: #ececea;
    --card: #ffffff;
    --ink: #1c1c1c;
    --logo-ink: #2a2a2a;
    --band: #2a8cc4;
    --band-light: #45a9dd;
    --band-dark: #1f79ad;
    --title-green: #5cb8a6;
    --contact-ink: #0f3550;
  }
  * { box-sizing: border-box; margin: 0; padding: 0; }
  html, body { width: 1200px; height: 576px; overflow: hidden; }
  body {
    background: var(--page);
    font-family: "Jost", "Futura", sans-serif;
    display: flex;
    align-items: center;
    justify-content: center;
    gap: 60px;
  }
  .card {
    position: relative;
    width: 525px;
    height: 300px;
    background: var(--card);
    box-shadow: 0 6px 18px rgba(0,0,0,0.12);
    overflow: hidden;
  }
  .logo-name {
    position: absolute;
    top: 58px;
    right: 44px;
    font-size: 30px;
    font-weight: 400;
    color: var(--logo-ink);
    letter-spacing: 0.5px;
  }
  /* Back side */
  .contact-band {
    position: absolute;
    left: 0;
    right: 0;
    top: 178px;
    height: 66px;
    background: var(--band);
    padding: 9px 0 0 28px;
  }
  .contact-line {
    display: flex;
    align-items: center;
    gap: 7px;
    font-size: 16px;
    font-weight: 400;
    color: var(--contact-ink);
    line-height: 24px;
  }
  .contact-line svg { width: 15px; height: 15px; flex: none; }
  /* Front side */
  .ribbon { position: absolute; inset: 0; width: 100%; height: 100%; }
  .holder-name {
    position: absolute;
    left: 38px;
    top: 124px;
    font-size: 25px;
    font-weight: 700;
    color: var(--ink);
  }
  .holder-title {
    position: absolute;
    left: 84px;
    top: 166px;
    font-size: 16px;
    font-weight: 300;
    color: var(--title-green);
  }
</style>
</head>
<body>
  <section class="card card-back" aria-label="Card back">
    <div class="logo-name">KTR Associates</div>
    <div class="contact-band">
      <p class="contact-line">
        <svg viewBox="0 0 16 16" aria-hidden="true"><rect x="1.5" y="3" width="13" height="10" fill="none" stroke="var(--title-green)" stroke-width="1.4"/><path d="M1.5 3.5 8 9l6.5-5.5" fill="none" stroke="var(--title-green)" stroke-width="1.4"/></svg>
        marta@ktr-associates.example
      </p>
      <p class="contact-line">
        <svg viewBox="0 0 16 16" aria-hidden="true"><path d="M4 1.5 6.3 4.5 5 6.3c.8 1.8 2.2 3.3 4 4.2l1.8-1.3 3 2.3-1.4 2.4C7.8 13.8 2.2 8.2 1.6 3z" fill="none" stroke="var(--title-green)" stroke-width="1.4" stroke-linejoin="round"/></svg>
        555-014-2286
      </p>
    </div>
  </section>

  <section class="card card-front" aria-label="Card front">
    <div class="logo-name">KTR Associates</div>
    <svg class="ribbon" viewBox="0 0 525 300" aria-hidden="true">
      <rect x="0" y="118" width="282" height="46" fill="var(--band)"/>
      <polygon points="282,118 318,150 318,196 282,164" fill="var(--band-light)"/>
      <rect x="318" y="150" width="72" height="46" fill="var(--band-dark)"/>
      <rect x="478" y="222" width="47" height="46" fill="var(--band)"/>
    </svg>
    <div class="holder-name">Marta Holbeck</div>
    <div class="holder-title">president</div>
  </section>
</body>
</html>
```